Business Card Design

We require a business card design for a law firm, our signature colours are maroon and cream. Our slogan is "From our family to yours", we would like the cards to be professional however feminine at the same time.

Industry/Entity Type

Business

Contact Information for Business Card

Helena Brackett & Associates Lawyers & Conveyancers, Helena Brackett LL.B. Principal Solicitor, 17 Quillon Street, Marrowdale NSW 2190

Logo styles of interest
Emblem Logo
Abstract Logo
Wordmark Logo

```html
<!DOCTYPE html>
<html lang="en">
<head>
<meta charset="utf-8">
<title>Helena Brackett &amp; Associates – Business Card</title>
<link rel="stylesheet" href="https://fonts.googleapis.com/css2?family=Tinos:wght@400&family=Jost:wght@300&display=swap">
<style>
  :root {
    --backdrop: #3b322d;
    --maroon-light: #8d161c;
    --maroon-dark: #6a0d12;
    --cream: #ecdcb9;
    --card-shadow: rgba(0, 0, 0, 0.45);
  }
  * { margin: 0; padding: 0; box-sizing: border-box; }
  html, body {
    width: 1200px;
    height: 1000px;
    overflow: hidden;
    background: var(--backdrop);
  }
  .canvas {
    position: relative;
    width: 1200px;
    height: 1000px;
    display: flex;
    align-items: center;
    justify-content: center;
  }
  .business-card {
    position: relative;
    width: 900px;
    height: 550px;
    background: linear-gradient(135deg, var(--maroon-light) 0%, var(--maroon-dark) 100%);
    box-shadow: 0 18px 40px var(--card-shadow);
    color: var(--cream);
  }
  .firm-lockup {
    position: absolute;
    top: 110px;
    left: 0;
    width: 100%;
    text-align: center;
  }
  .firm-mark {
    display: block;
    margin: 0 auto 22px;
  }
  .firm-name {
    font-family: "Tinos", "Times New Roman", serif;
    font-weight: 400;
    font-size: 40px;
    line-height: 1.1;
    color: var(--cream);
  }
  .firm-type {
    font-family: "Tinos", "Times New Roman", serif;
    font-weight: 400;
    font-size: 26px;
    margin-top: 6px;
    color: var(--cream);
  }
  .contact-line {
    position: absolute;
    left: 40px;
    right: 40px;
    bottom: 60px;
    font-family: "Jost", "Futura", sans-serif;
    font-weight: 300;
    font-size: 21px;
    letter-spacing: 1.6px;
    white-space: nowrap;
    color: var(--cream);
  }
</style>
</head>
<body>
  <main class="canvas">
    <article class="business-card">
      <div class="firm-lockup">
        <svg class="firm-mark" width="70" height="70" viewBox="0 0 70 70" aria-hidden="true">
          <circle cx="35" cy="35" r="30" fill="none" stroke="var(--cream)" stroke-width="3"/>
        </svg>
        <h1 class="firm-name">Helena Brackett &amp; Associates</h1>
        <p class="firm-type">Lawyers</p>
      </div>
      <p class="contact-line">Helena Brackett LL.B. Principal Solicitor, 17 Quillon Street, Marrowdale NSW 2190</p>
    </article>
  </main>
</body>
</html>
```